Flyer-Design für Unternehmensberatung
Zielgruppe
Unternehmensberatung und biete Beratung zur Gründung, Marketing, Kundengewinnung und Kooperation. Meine Zielgruppe sind Heilpraktikerinnen und Heilpraktiker für Psychotherapie, die Ihre Praxis gründen, meist ab 45 Jahre.
Aufgabenstellung
Der Flyer soll in einen Umschlag von 22 x 11 cm passen. Die Farben vom Logo bitte berücksichtigen.

```html
<!DOCTYPE html>
<html lang="de">
<head>
<meta charset="utf-8">
<title>Flyer – Brandt Organisation</title>
<link href="https://fonts.googleapis.com/css2?family=Oswald:wght@500;700&family=Open+Sans:wght@400;600;700&display=swap" rel="stylesheet">
<style>
:root{
  --red-dark:#9a210c;
  --red:#c0300f;
  --red-light:#dc4418;
  --red-accent:#d81f2a;
  --grey:#5d5d5d;
  --white:#ffffff;
  --ink:#222222;
  --bg:#e4e5e7;
}
*{box-sizing:border-box;margin:0;padding:0}
html,body{width:1200px;height:2386px;overflow:hidden;background:var(--bg)}
body{font-family:"Open Sans",Arial,sans-serif;color:var(--white);position:relative}
.spread{position:absolute;left:60px;width:1080px;height:764px;display:flex;box-shadow:0 6px 24px rgba(0,0,0,.18)}
.spread--outside{top:150px}
.spread--inside{top:1300px}
.panel{position:relative;width:360px;height:764px;overflow:hidden;
  background:linear-gradient(160deg,var(--red-dark) 0%,var(--red) 45%,var(--red-light) 100%)}
.panel+.panel{border-left:1px solid rgba(0,0,0,.12)}
.deco{position:absolute;inset:0;width:100%;height:100%}
.photo{position:absolute}
.photo--portrait{left:36px;top:0;width:324px;height:300px;
  background:linear-gradient(135deg,#cfe3ea,#f1ece6 50%,#d9c7b4);
  clip-path:polygon(0 0,100% 0,100% 100%,22% 100%,0 78%)}
.photo--cover{left:0;top:0;width:360px;height:580px;
  background:radial-gradient(ellipse at 50% 40%,#e0573a 0%,#c23614 55%,#a8270d 100%)}
.photo--couple{left:0;top:470px;width:270px;height:294px;
  background:linear-gradient(135deg,#e9e9ea,#c9d5e3 50%,#b9a893);
  clip-path:polygon(0 0,100% 100%,0 100%)}
.photo--success{left:0;top:0;width:360px;height:440px;
  background:radial-gradient(circle at 70% 45%,#ffd07a 0%,#f09040 35%,#b8401c 75%,#8f2a12 100%);
  clip-path:polygon(0 30%,28% 0,100% 0,100% 100%)}
.name{position:absolute;left:28px;top:346px;font-family:"Oswald",Arial,sans-serif;font-weight:700;font-size:22px;letter-spacing:.5px}
.bio{position:absolute;left:28px;right:26px;top:388px;font-size:11.5px;line-height:1.5}
.bio p+p{margin-top:12px}
.contact{position:absolute;left:0;right:0;top:300px;text-align:center;font-size:13.5px;line-height:2.05}
.contact h2{font-family:"Open Sans",Arial,sans-serif;font-weight:700;font-size:22px;letter-spacing:1px;line-height:1.6;margin-bottom:4px}
.brand-strip{position:absolute;left:0;right:0;bottom:0;height:170px;background:var(--white);display:flex;align-items:center;justify-content:center;gap:12px}
.brand-mark{width:18px;height:18px;background:var(--red-accent)}
.brand-name{font-family:"Open Sans",Arial,sans-serif;font-weight:700;font-size:19px;color:var(--ink);letter-spacing:.3px}
.brand-tag{display:block;font-weight:700;font-size:11px;color:var(--ink);letter-spacing:0}
.headline{position:absolute;left:22px;bottom:28px;font-family:"Oswald",Arial,sans-serif;font-weight:700;font-size:40px;line-height:1.18;text-transform:uppercase}
.copy{position:absolute;font-size:13px;line-height:1.55}
.copy p+p{margin-top:14px}
.copy strong{font-weight:700}
.copy--intro{left:26px;right:24px;top:36px}
.copy--projects{left:26px;right:22px;top:320px;font-size:14px;line-height:1.45}
.copy--projects h3{font-size:16px;font-weight:700;line-height:1.25;margin-bottom:12px}
.copy--projects p+p{margin-top:8px}
.copy--results{left:24px;right:26px;top:470px;font-size:12.5px;line-height:1.5}
</style>
</head>
<body>

<section class="spread spread--outside" aria-label="Außenseite">
  <article class="panel panel--about">
    <div class="photo photo--portrait" role="img" aria-label="Porträtfoto der Beraterin Helga Brandt"></div>
    <svg class="deco" viewBox="0 0 360 764" aria-hidden="true">
      <polygon points="0,200 14,200 114,310 100,310" fill="var(--grey)"/>
      <polygon points="0,226 8,226 96,322 88,322" fill="var(--red-accent)"/>
    </svg>
    <h2 class="name">HELGA BRANDT</h2>
    <div class="bio">
      <p>Ihr Erfahrungsspektrum liegt in der ganzheitlichen Beratung von Selbstständigen von der Idee, über die Angebotserstellung und das Marketing, bis zum ersten Kunden. Ihre beruflichen Wurzeln liegen in medizinischen Bereichen und als Beraterin im Qualitätsmanagement von Industrieunternehmen. Ihre Unternehmensberatung gründet sie in 2011. Sie steigt nach dem wirtschaftswissenschaftlichen Studium als Beraterin ein.</p>
      <p>Mit Ihrem umfassenden Wissen und Kenntnisstand gelingt Ihr die ganzheitliche Sicht auf Kleinunternehmen und Praxen, auch bei Beginn einer Selbstständigkeit. Viele positive Rückmeldungen Ihrer Kunden bestärken sie weiterhin auf dem Fachgebiet zu beraten.</p>
      <p>Als ehemalige Vizepräsidentin in einem Wirtschaftsverband begleitete sie einige Jahre die Unternehmer und Selbstständigen mit Wissen, Themen und Vorträgen rund um die Selbstständigkeit, Gründung und Kooperation.</p>
    </div>
  </article>

  <article class="panel panel--contact">
    <div class="contact">
      <h2>KONTAKT</h2>
      Helga Brandt, Diplom-Kauffrau<br>
      Am Lindenhang 4/2<br>
      71299 Talheim am See<br>
      Telefon 07031 48260<br>
      Mobil 0152 38471920<br>
      info@brandt-organisation.de<br>
      www.brandt-organisation.de
    </div>
    <div class="brand-strip">
      <span class="brand-mark"></span>
      <span class="brand-name">BRANDT ORGANISATION<span class="brand-tag">Projekt- und Change Management</span></span>
    </div>
  </article>

  <article class="panel panel--cover">
    <div class="photo photo--cover" role="img" aria-label="Foto einer überraschten jungen Frau mit Smartphone in den Händen"></div>
    <h1 class="headline">Patienten mit<br>Leichtigkeit<br>gewinnen</h1>
  </article>
</section>

<section class="spread spread--inside" aria-label="Innenseite">
  <article class="panel panel--intro">
    <div class="copy copy--intro">
      <p>Ihre Praxisräume sind eingerichtet und keiner ruft Sie an. Vergeblich hoffen Sie auf neue Patienten. Nach zwei Tagen die ersten Patienten gewinnen und somit kontinuierlich Patienten gewinnen. Sie als praktizierende Heilpraktikerin planen das auch?</p>
      <p>Mein erweitertes Intensiv-Angebot sind 2 x 2 Stunden Marketing- und Kooperationsberatung: Analyse, Beratung und Optimierung.</p>
      <p><strong>Sie erfahren in einem kostenfreien Erstgespräch was möglich ist. Vereinbaren Sie einen Termin!</strong></p>
    </div>
    <svg class="deco" viewBox="0 0 360 764" aria-hidden="true">
      <polygon points="0,400 0,764 360,764" fill="var(--white)"/>
      <polygon points="70,430 100,430 360,700 360,764 330,764" fill="var(--grey)"/>
      <polygon points="118,430 132,430 360,668 360,684" fill="var(--red-accent)"/>
    </svg>
    <div class="photo photo--couple" role="img" aria-label="Foto eines lächelnden älteren Paares beim Beratungsgespräch"></div>
  </article>

  <article class="panel panel--projects">
    <svg class="deco" viewBox="0 0 360 764" aria-hidden="true">
      <polygon points="200,0 360,0 360,190" fill="var(--grey)"/>
      <polygon points="160,0 186,0 360,206 360,236" fill="var(--red-accent)"/>
      <polygon points="0,560 0,764 80,764" fill="var(--grey)"/>
    </svg>
    <div class="copy copy--projects">
      <h3>Erfolgreich abgeschlossene Projekte im Gesundheitsbereich:</h3>
      <p>Patientengewinnung und Aufbau der eigenen Selbstständigkeit im Gesundheitsbereich</p>
      <p><strong>Die Aufträge:</strong> Marketing für den Praxisaufbau nach Gründung</p>
      <p>Beratungsumfang: 4 Stunden</p>
      <p><strong>Ausgangslage:</strong> Die Praxisräume waren vorhanden. Noch keine Patienten in der Praxis, kein Flyer, keine Webseite, keine Visitenkarte vorhanden.</p>
      <p><strong>Ziele meiner Kundinnen:</strong> Patienten für die Privat-Praxis gewinnen und auffinden geeigneter Kooperationspartner</p>
    </div>
  </article>

  <article class="panel panel--results">
    <div class="photo photo--success" role="img" aria-label="Foto einer jubelnden Person als Silhouette vor Sonnenuntergang"></div>
    <svg class="deco" viewBox="0 0 360 764" aria-hidden="true">
      <polygon points="0,0 30,0 0,40" fill="var(--grey)"/>
      <polygon points="100,0 112,0 360,400 360,420" fill="var(--red-accent)"/>
      <polygon points="300,380 330,360 360,400 360,440" fill="var(--grey)"/>
    </svg>
    <div class="copy copy--results">
      <p>Maßnahmen zur Patientengewinnung festgelegt, Spezialisierung, Text und Bildervorschläge für ersten Flyer und Visitenkarten. Themen für die Webseite erarbeitet. Maßnahmen festgelegt, um Kooperationspartner zu gewinnen, Inhalte für eigene Webseite festgelegt, Plattformen für Veröffentlichung.</p>
      <p><strong>Ergebnisse bei Kundinnen:</strong> nach 2 Tagen, die ersten Patienten gewonnen und heute kontinuierliche Patientengewinnung.</p>
      <p><strong>Interessiert?<br>Rufen Sie mich an: 07031 48260</strong></p>
    </div>
  </article>
</section>

</body>
</html>
```